Neues Corporate Identity Web Design für einen coolen Energydrink
Zielgruppe
UPDATE: das BETA storyboard für das Video auf der neuen Seite.. jetzt in den Dateien, hier fehlt noch der sportliche dynamische abenteurliche part.. wird die tage erneut geupdatet..
Hallo Designer,
wir sind Velunora - ein junges Start-Up, die 'Guayusa - den Energydrink der Indianer' nach Deutschland gebracht haben. Mit unseren Produkten sprechen wir Backpacker / Abenteurer, Gesundheitsbewusste, Spirituelle, Kreative, Startups, Surfer, Skater, Weltverbesserer, Hipster und später auch Sportler und Gamer an. Und klaro auch die Energydrink und Kaffeejunkies ;-) ...
Aufgabenstellung
Neues Corporate Identity Design für eine Wordpress Seite mit Shop Funktion (Woocomerce)
Ihr findet eine PDF in den Dateien mit den genauen Wünschen von uns. -> BITTE LESEN!
Bilder könnt Ihr aus den bestehenden Auftritten entnehmen. Ihr findet diese auf unser Webseite: www.velunora.de auf unserem Plauderplatz Account: www.facebook.com/Kolarintee/ auf unserem Instagram Account: www.instagram.com/velunora als auch auf unseren Produktseiten auf Kaufstadt. Weitere Bilder können aus bildervorrat-beispiel.de vorgeschlagen werden.
Die von uns verwendete Schriftart haben wir auch angehängt, ist aber kein Muss, wenn ihr andere Ideen habt, her damit!
Dateiübergabe in PSD Form, so das ein Webdesigner es gut umsetzen kann.

```html
<!DOCTYPE html>
<html lang="de">
<head>
<meta charset="utf-8">
<title>Velunora Webdesign Moodboard</title>
<link href="https://fonts.googleapis.com/css2?family=Lato:ital,wght@0,400;0,700;1,400&family=Lexend:wght@500;700&family=Raleway:ital,wght@0,400;0,700;1,400&display=swap" rel="stylesheet">
<style>
  :root {
    --tan: #DEB58C;
    --charcoal: #3C3C3B;
    --lime: #99B915;
    --text: #3C3C3B;
    --muted: #555555;
    --paper: #ffffff;
    --ornament-dark: #4a4a49;
    --ornament-light: #a9a9a8;
  }
  * { margin: 0; padding: 0; box-sizing: border-box; }
  html, body { width: 1200px; height: 2419px; overflow: hidden; background: var(--paper); }
  .board { position: relative; width: 1200px; height: 2419px; font-family: "Lato", sans-serif; color: var(--text); }
  .abs { position: absolute; }

  .board-title { left: 0; width: 1200px; top: 78px; text-align: center; font-size: 27px; line-height: 29px; letter-spacing: 0.5px; font-weight: 400; }
  .section-label { font-size: 19px; color: var(--tan); letter-spacing: 0.3px; font-weight: 400; }
  .impression { left: 220px; top: 262px; font-size: 19px; color: var(--muted); }

  .swatch { width: 185px; height: 157px; color: #fff; font-size: 16px; padding: 0 0 14px 15px; display: flex; align-items: flex-end; }
  .swatch--tan { left: 220px; top: 413px; background: var(--tan); }
  .swatch--charcoal { left: 434px; top: 413px; background: var(--charcoal); }
  .swatch--lime { left: 220px; top: 602px; background: var(--lime); }

  .font-name { left: 709px; font-size: 19px; }
  .sample { left: 735px; width: 318px; }
  .sample-caption { font-family: "Raleway", sans-serif; font-style: italic; font-size: 13px; display: block; text-align: left; font-weight: 400; font-variant: normal; }
  .neusa { font-family: "Lexend", sans-serif; font-size: 18.5px; letter-spacing: 0.2px; line-height: 21px; }
  .neusa--bold { font-weight: 700; }
  .neusa--medium { font-weight: 500; }
  .raleway { font-family: "Raleway", sans-serif; font-size: 16.5px; line-height: 19.5px; }
  .raleway .line { display: block; white-space: nowrap; }
  .raleway .line--full { text-align: justify; text-align-last: justify; }
  .raleway--bold { font-weight: 700; font-size: 17px; }
  .raleway--caps { font-variant: small-caps; font-size: 16px; }

  .photo { width: 252px; height: 252px; border-radius: 50%; }
  .photo--mountains { left: 414px; top: 893px; background: linear-gradient(180deg, #c9a894 0%, #a7b8ac 40%, #6f8f7a 62%, #3e5a2a 85%, #2c4218 100%); }
  .photo--hiker { left: 736px; top: 893px; background: radial-gradient(circle at 35% 40%, #c69779 0%, #9a8a78 30%, #6c7d5c 60%, #3e5a38 100%); }
  .photo--hills { left: 414px; top: 1193px; background: radial-gradient(circle at 50% 25%, #f3e3a8 0%, #b9b044 30%, #8c9a2c 60%, #5f6b1c 100%); }
  .photo--writing { left: 736px; top: 1193px; background: linear-gradient(160deg, #6b6a3e 0%, #b89a80 35%, #e6e6ea 55%, #9a4a2a 80%, #2f5e3a 100%); }

  .ornament-band { left: 220px; top: 1636px; width: 174px; height: 545px; background: linear-gradient(180deg, var(--ornament-dark) 0%, var(--ornament-light) 22%, var(--ornament-dark) 45%, var(--ornament-light) 68%, var(--ornament-dark) 100%); }
  .ornament-leaf { left: 478px; top: 1643px; width: 60px; height: 84px; background: linear-gradient(135deg, #b3cf2c 0%, var(--lime) 100%); border-radius: 60% 8% 60% 8%; }
  .ornament-diamond { left: 445px; top: 1779px; width: 123px; height: 73px; background: linear-gradient(90deg, var(--ornament-light), var(--ornament-dark) 50%, var(--ornament-light)); clip-path: polygon(50% 0, 100% 50%, 50% 100%, 0 50%); }
  .ornament-figure { left: 475px; top: 1918px; width: 80px; height: 87px; background: radial-gradient(circle, var(--ornament-dark) 0%, var(--ornament-light) 100%); border-radius: 40%; }
  .ornament-triangle { left: 473px; top: 2068px; width: 84px; height: 75px; background: linear-gradient(180deg, var(--ornament-dark), var(--ornament-light)); clip-path: polygon(0 20%, 100% 20%, 50% 100%); }

  .icon-row { left: 735px; display: flex; align-items: flex-end; }
  .icon-row span { font-size: 13.5px; letter-spacing: 0.8px; color: var(--text); }
  .badge { position: absolute; left: 44px; top: -6px; width: 30px; height: 30px; border-radius: 50%; background: var(--lime); color: #fff; font-family: "Raleway", sans-serif; font-size: 18px; text-align: center; line-height: 30px; }

  .social { top: 2265px; width: 55px; height: 55px; border-radius: 50%; border: 2px solid var(--tan); }
  .social-name { top: 2326px; width: 90px; text-align: center; font-size: 10px; color: var(--tan); }
</style>
</head>
<body>
<main class="board">
  <h1 class="abs board-title">VELUNORA WEBDESIGN<br>MOODBOARD</h1>

  <h2 class="abs section-label" style="left:220px;top:229px;">EINDRUCK</h2>
  <p class="abs impression">frisch |&nbsp; modern &nbsp;| &nbsp;organic &nbsp;| &nbsp;etnic</p>

  <h2 class="abs section-label" style="left:220px;top:354px;">HAUPTFARBEN</h2>
  <div class="abs swatch swatch--tan">#DEB58C</div>
  <div class="abs swatch swatch--charcoal">#3C3C3B</div>
  <div class="abs swatch swatch--lime">#2997D4</div>

  <h2 class="abs section-label" style="left:709px;top:361px;">FONT</h2>
  <p class="abs font-name" style="top:401px;">NEUSA NEXT PRO <b>-</b> highlights</p>
  <p class="abs sample" style="top:429px;"><span class="neusa neusa--bold">Energy Kick aus dem Amazonas</span><span class="sample-caption">Wide Bold</span></p>
  <p class="abs sample" style="top:486px;"><span class="neusa neusa--medium">Energy Kick aus dem Amazonas</span><span class="sample-caption">Wide Medium</span></p>

  <p class="abs font-name" style="top:548px;">RALEWAY</p>
  <p class="abs sample raleway" style="top:576px;">
    <span class="line">Er trank Guayusa und so ist er mit einem</span>
    <span class="line">Auge in dieser Welt und mit dem ande-</span>
    <span class="line">ren in der „Anderen Welt.“</span>
    <span class="sample-caption">Regular</span>
  </p>
  <p class="abs sample raleway raleway--bold" style="top:666px;">
    <span class="line line--full">Er trank Guayusa und so ist er mit</span>
    <span class="line line--full">einem Auge in dieser Welt und mit dem</span>
    <span class="line">anderen in der „Anderen Welt.“</span>
    <span class="sample-caption">Bold</span>
  </p>
  <p class="abs sample raleway raleway--caps" style="left:740px;top:756px;width:316px;">
    <span class="line line--full">Er trank Guayusa und so ist er mit</span>
    <span class="line line--full">einem Auge in dieser Welt und mit dem</span>
    <span class="line">anderen in der „Anderen Welt.“</span>
    <span class="sample-caption">Small Capital</span>
  </p>

  <h2 class="abs section-label" style="left:220px;top:900px;">HINTERGRÜNDE</h2>
  <div class="abs photo photo--mountains" role="img" aria-label="Nebelige Berglandschaft mit grünen Teeplantagen"></div>
  <div class="abs photo photo--hiker" role="img" aria-label="Wanderer mit Rucksack in der Natur"></div>
  <div class="abs photo photo--hills" role="img" aria-label="Sonnige grüne Teehügel"></div>
  <div class="abs photo photo--writing" role="img" aria-label="Hand schreibt Notizen auf einem bunt gemusterten Tuch"></div>

  <h2 class="abs section-label" style="left:220px;top:1559px;">DESIGN ELEMENTS</h2>
  <div class="abs ornament-band" role="img" aria-label="Gestapelte ethnische Musterbänder aus Rauten, Dreiecken und Zickzacklinien"></div>
  <div class="abs ornament-leaf" role="img" aria-label="Grünes Blatt"></div>
  <div class="abs ornament-diamond" role="img" aria-label="Ethnisches Rautenornament"></div>
  <div class="abs ornament-figure" role="img" aria-label="Stilisierte Eidechsenfigur im Ethno-Stil"></div>
  <div class="abs ornament-triangle" role="img" aria-label="Geometrisches Dreiecksornament"></div>

  <h2 class="abs section-label" style="left:735px;top:1563px;">ICONS</h2>

  <div class="abs icon-row" style="top:1644px;">
    <svg width="50" height="52" viewBox="0 0 50 52"><circle cx="25" cy="14" r="13" fill="var(--tan)"/><path d="M0 52 Q2 30 25 30 Q48 30 50 52Z" fill="var(--tan)"/></svg>
    <span style="margin-left:13px;">PROFILE</span>
  </div>
  <div class="abs icon-row" style="top:1737px;">
    <svg width="50" height="52" viewBox="0 0 50 52"><circle cx="20" cy="20" r="16" fill="none" stroke="var(--tan)" stroke-width="5"/><line x1="32" y1="32" x2="47" y2="49" stroke="var(--tan)" stroke-width="6" stroke-linecap="round"/></svg>
    <span style="margin-left:13px;">SUCHEN</span>
  </div>
  <div class="abs icon-row" style="top:1825px;left:740px;">
    <svg width="46" height="46" viewBox="0 0 50 46"><path d="M2 3 H10 L16 28 H42 L47 11 H13" fill="none" stroke="var(--tan)" stroke-width="4" stroke-linejoin="round"/><rect x="14" y="12" width="31" height="14" fill="var(--tan)"/><circle cx="18" cy="39" r="4" fill="var(--tan)"/><circle cx="38" cy="39" r="4" fill="var(--tan)"/></svg>
    <span style="margin-left:13px;">WARENKORB - LEER</span>
  </div>
  <div class="abs icon-row" style="top:1910px;left:745px;">
    <svg width="42" height="42" viewBox="0 0 50 46"><path d="M2 3 H10 L16 28 H42 L47 11 H13" fill="none" stroke="var(--tan)" stroke-width="4" stroke-linejoin="round"/><rect x="14" y="12" width="31" height="14" fill="var(--tan)"/><circle cx="18" cy="39" r="4" fill="var(--tan)"/><circle cx="38" cy="39" r="4" fill="var(--tan)"/></svg>
    <div class="badge" style="left:33px;top:-16px;">2</div>
    <span style="margin-left:17px;">WARENKORB - MIT PRODUKTE</span>
  </div>
  <div class="abs icon-row" style="top:1995px;left:752px;">
    <svg width="42" height="42" viewBox="0 0 42 42"><path d="M8 4 L15 12 L11 17 Q15 25 22 30 L27 26 L35 33 L30 39 Q14 36 3 12 Z" fill="var(--tan)"/><path d="M22 6 Q32 8 34 18" fill="none" stroke="var(--tan)" stroke-width="2.5"/><path d="M22 0 Q38 2 40 18" fill="none" stroke="var(--tan)" stroke-width="2.5"/></svg>
    <span style="margin-left:14px;">KONTAKT - TELEFON</span>
  </div>

  <h2 class="abs section-label" style="left:220px;top:2276px;">SOCIAL MEDIA</h2>
  <div class="abs social" style="left:404px;"></div>
  <div class="abs social-name" style="left:386px;">Plauderplatz</div>
  <div class="abs social" style="left:481px;"></div>
  <div class="abs social-name" style="left:463px;">Zwitscherdraht</div>
  <div class="abs social" style="left:558px;"></div>
  <div class="abs social-name" style="left:540px;">Netzwerkstube</div>
</main>
</body>
</html>
```